Velmora Responsive Website Redesign

We need a web site design for our music marketing company. We provide musicians, artists, rappers, records labels a way to help them market an promote there music.

PLEASE NOTE THE BOOTSTRAP THEME WE ARE USING
PLEASE NOTE THE WIREFRAME FOR THE PAGES I HAVE INCLUDED
WE ARE LOOKING FOR THE DASHBOARD PAGE, BUT IF YOU HAVE TIME and WANT TO SHOW US A CONCEPT FOR THIS HOME PAGE. PLEASE DO (see home.jpg)

This site will will allow artists to register, upload their music, create a profile and then promote their music across our various mobile and social properties.

Here is the bootstrap theme we are planning to use. This page is something like what the artists should see when they login

http://quortexthemes.net/palvane_panel-v4.1/

Here are some examples of sites we like (look and feel):

www.brelvox.com (music site, edgy, dark colors, great consumer site for music)
yarmeo.com (clean design, easy to get around)
tundravox.com (leading artists upload site)
plimbo.com (great navigation and site leads the user to an end point --> invest money)

I would like to see your design skills to make this theme. I have uploaded the homepage and the logged in page. Remember this is a responsive site, so the webpage should be designed with that intention.

I have provide files (wireframes) to give you direction on some possibilities for the design you are creating.

dashboard.jpg - this page is what the artists will see when he logs in. the homepage is very simple so this is not something that I will ask you do design now.

History
Here is some history about our business:
1. Founded in 2002
2. Our last site was more of a social marketing site that registered about 20,000 artists
3. That site didn't make any money and it was costly to maintain
4. Artists registered for free and not many signed up for our premium services
5. We offered a lot of different services and weren't really good at anyone thing for artists.

To see an old version of our site go here:
https://oldpages.example.org/snap/20150207122208/http://www.velmora.biz/

Its because of this that we shut the site down and decided to redesign it

Next Steps
A. Design Build a better website
B. Have the website that sells 1 or 2 things, and do that better than any other site
C. Focus on registering artists, offering them services that they want, and make it easy for them to find these services once they are in our site.

Other items
200,000 facebook likes (www.friendloop.example/velmorabiz)
85,000 Twitter followers (www.friendloop.example/velmroa)

Files I have provided:
Content - there is no content at this point
Updates

Please note this project is to redesign velmora.biz using the information I provided in the brief. WE ARE NOT REDESIGNING THE WORDRPESS SITE (velmora.hostquill.net). This site is only to be used for getting the logo. WE ARE BUILDING A NEW Website for velmora.biz. I have provided:1. Wiresframes of what is neede (see dashboard.jpg)2. A link to the bootstrap theme we will be usingPlease review the brief again. I DO LIKE YOUR DESIGNS. Its just not what this project is for. Petra Added Thursday, October 1, 2015

Target Market(s)

Musician,
Records Labels,
Indie Artists
Unsigned Artists / Bands

Industry/Entity Type

Artists

Number of Pages Required

2 page

Font styles to use
Other font styles liked:
• Google Lato or Helvetica,

Requirements
Must have
• We are using a theme (see the brief above), but the site should have its own distinct look and feel
• Clear navigation (big buttons, and call to actions)
• The site should focus on driving member to register and by services from us

```html
<!DOCTYPE html>
<html lang="en">
<head>
<meta charset="utf-8">
<title>Velmora – Artist Dashboard</title>
<link rel="stylesheet" href="https://fonts.googleapis.com/css2?family=Lato:wght@400;700;900&display=swap">
<style>
  :root {
    --sidebar: #2b3b4c;
    --sidebar-text: #c9d3dd;
    --sidebar-sub: #9fb0c0;
    --page: #eef0f2;
    --panel: #ffffff;
    --ink: #2f3338;
    --muted: #6d737a;
    --teal: #1ab394;
    --blue: #1c84c6;
    --yellow: #f8c51c;
    --dark-btn: #2f3338;
    --orange: #f0932b;
    --red: #e04b4b;
  }
  * { box-sizing: border-box; margin: 0; padding: 0; }
  html, body { width: 872px; height: 1200px; overflow: hidden; }
  body { font-family: "Lato", Helvetica, Arial, sans-serif; background: var(--page); color: var(--ink); position: relative; }

  .sidebar { position: absolute; left: 0; top: 0; width: 196px; height: 1200px; background: var(--sidebar); color: var(--sidebar-text); padding: 18px 16px; }
  .brand { display: flex; align-items: center; gap: 8px; font-weight: 900; font-size: 20px; color: #fff; }
  .brand-mark { width: 14px; height: 14px; background: var(--teal); }
  .user { display: flex; align-items: center; gap: 10px; margin: 28px 0 22px; }
  .avatar { width: 40px; height: 40px; border-radius: 50%; background: linear-gradient(135deg, #8a96a3, #5d6976); }
  .user-name { font-size: 12px; color: #fff; }
  .nav { list-style: none; font-size: 13px; }
  .nav > li { margin-bottom: 14px; }
  .nav .active { color: #fff; font-weight: 700; }
  .subnav { list-style: none; margin: 6px 0 0 12px; font-size: 11px; color: var(--sidebar-sub); }
  .subnav li { margin-bottom: 4px; }

  .main { position: absolute; left: 196px; top: 0; width: 676px; padding: 14px 16px; }
  .panel { background: var(--panel); margin-bottom: 14px; padding: 18px 22px; width: 100%; }
  .panel-title { font-size: 22px; font-weight: 700; color: var(--ink); }

  .btn { display: inline-block; font-family: inherit; font-size: 11px; padding: 8px 18px; border: 0; color: #fff; white-space: nowrap; }
  .btn-dark { background: var(--dark-btn); margin-right: 8px; }
  .btn-yellow { background: var(--yellow); }
  .btn-blue { background: var(--blue); }

  .notification { height: 160px; }
  .notification p { font-size: 11px; line-height: 1.5; color: var(--muted); margin: 8px 0 14px; width: 430px; }

  .profile { height: 135px; display: flex; flex-direction: column; }
  .progress { margin-top: 18px; height: 12px; width: 540px; background: #e6e9ec; }
  .progress-fill { width: 60%; height: 100%; background: linear-gradient(90deg, #3bb6e8, #7fd27a, #d7e34d); }
  .progress-labels { position: relative; width: 540px; height: 12px; font-size: 9px; color: var(--muted); margin-top: 3px; }
  .progress-labels span:nth-child(2) { position: absolute; left: 312px; }
  .profile .btn { align-self: flex-end; margin-top: 8px; }

  .upload { display: flex; justify-content: space-between; align-items: center; height: 110px; }
  .upload .panel-title { font-size: 20px; white-space: nowrap; }

  .metrics { height: 225px; }
  .metrics .panel-title { color: var(--teal); font-size: 19px; }
  .metrics-body { display: flex; align-items: center; margin-top: 22px; }
  .songs { list-style: none; width: 200px; font-size: 10px; }
  .songs li { display: flex; align-items: center; gap: 8px; margin-bottom: 18px; }
  .check { width: 14px; height: 14px; border: 1px solid #9aa2ab; }
  .check.done { background: var(--teal); border-color: var(--teal); }
  .s-active { color: var(--teal); }
  .s-pending { color: var(--orange); }
  .s-done { color: var(--red); }
  .view-all { font-size: 10px; color: var(--blue); margin-left: 22px; }

  .promo { display: flex; align-items: center; height: 235px; padding: 0 0 0 40px; }
  .promo-photo { width: 230px; height: 220px; align-self: flex-end; background: linear-gradient(135deg, #f4f4f4, #c9cdd1); }
  .promo-text { padding-left: 26px; text-align: center; }
  .promo-text h2 { font-size: 18px; font-weight: 700; color: #3a3f45; }
  .promo-text h3 { font-size: 17px; font-weight: 700; color: #3a3f45; margin-top: 16px; white-space: nowrap; }

  .cards { display: flex; justify-content: space-between; padding: 14px 22px; height: 210px; }
  .card { width: 188px; }
  .card-head { background: var(--teal); color: #fff; font-size: 9px; padding: 4px 6px; }
  .card-img { height: 166px; }
  .card-img.one { background: linear-gradient(160deg, #a07a5a, #3d2c22); }
  .card-img.two { background: linear-gradient(160deg, #c8c4be, #5e5a55); }
  .card-img.three { background: linear-gradient(160deg, #e3d7c8, #9b8a76); }

  .footer { position: absolute; left: 196px; right: 0; top: 1172px; height: 28px; padding: 8px 32px; font-size: 10px; color: var(--muted); display: flex; justify-content: space-between; background: var(--panel); }
</style>
</head>
<body>
  <aside class="sidebar">
    <div class="brand"><span class="brand-mark"></span>Velmora</div>
    <div class="user">
      <div class="avatar" role="img" aria-label="Artist profile photo"></div>
      <span class="user-name">Artist Name</span>
    </div>
    <ul class="nav">
      <li class="active">Dashboard</li>
      <li>My Profile
        <ul class="subnav"><li>Profile</li><li>Biography</li><li>Social Links</li><li>Payment History</li><li>Notification</li></ul>
      </li>
      <li>Market &amp; Promote
        <ul class="subnav"><li>Create New Campaign</li><li>View Existing Campaign</li></ul>
      </li>
      <li>My Music
        <ul class="subnav"><li>Upload</li><li>Manage</li></ul>
      </li>
      <li>My Videos
        <ul class="subnav"><li>Upload</li><li>Manage</li></ul>
      </li>
      <li>Settings</li>
      <li>Invite Friends</li>
      <li>Logout</li>
    </ul>
  </aside>

  <main class="main">
    <section class="panel notification">
      <h1 class="panel-title">Notification</h1>
      <p>Welcome back to your artist space. Your account is active and new tools are ready to help you reach more listeners. Check your profile, upload fresh tracks and start a campaign today to grow your fans.</p>
      <span class="btn btn-dark">Close this message</span><span class="btn btn-yellow">Proceed to next step</span>
    </section>

    <section class="panel profile">
      <h2 class="panel-title">Almost there ! Please Complete your Profile...</h2>
      <div class="progress"><div class="progress-fill"></div></div>
      <div class="progress-labels"><span>0%</span><span>60%</span></div>
      <span class="btn btn-blue">Update your profile</span>
    </section>

    <section class="panel upload">
      <h2 class="panel-title">Let's upload your songs, and videos (3)</h2>
      <span class="btn btn-blue">Upload Your Music</span>
    </section>

    <section class="panel metrics">
      <h2 class="panel-title">Performance &amp; Metrics</h2>
      <div class="metrics-body">
        <div>
          <ul class="songs">
            <li><span class="check"></span>Song 1 Name <span class="s-active">Active</span></li>
            <li><span class="check"></span>Song 2 Name <span class="s-pending">Pending</span></li>
            <li><span class="check done"></span>Song 3 Name <span class="s-done">Completed</span></li>
          </ul>
          <span class="view-all">View All</span>
        </div>
        <svg width="400" height="100" viewBox="0 0 400 100" aria-label="Performance line chart">
          <polyline fill="none" stroke="#1ab394" stroke-width="2.5" points="10,30 60,48 100,52 140,66 180,40 220,20 260,24 300,12 340,36"/>
          <g fill="#fff" stroke="#1ab394" stroke-width="2">
            <circle cx="60" cy="48" r="3"/><circle cx="100" cy="52" r="3"/><circle cx="140" cy="66" r="3"/>
            <circle cx="180" cy="40" r="3"/><circle cx="220" cy="20" r="3"/><circle cx="260" cy="24" r="3"/>
            <circle cx="300" cy="12" r="3"/><circle cx="340" cy="36" r="3"/>
          </g>
        </svg>
      </div>
    </section>

    <section class="panel promo">
      <div class="promo-photo" role="img" aria-label="Photo of a musician wearing headphones at a mixing desk"></div>
      <div class="promo-text">
        <h2>Market &amp; Promote your music Now</h2>
        <h3>Now, Let's getting people talking about your music</h3>
      </div>
    </section>

    <section class="panel cards">
      <article class="card"><div class="card-head">Grow Your Fanbase With Campaigns</div><div class="card-img one" role="img" aria-label="Photo of a performer on stage"></div></article>
      <article class="card"><div class="card-head">Share Your Songs On Social</div><div class="card-img two" role="img" aria-label="Photo of a singer with long hair"></div></article>
      <article class="card"><div class="card-head">Featured Artist</div><div class="card-img three" role="img" aria-label="Photo of a woman listening to music"></div></article>
    </section>
  </main>

  <footer class="footer"><span>© 2015 Velmora, Inc. All rights reserved.</span><span>↑</span></footer>
</body>
</html>
```